FROSTVITAL

We need 2 different business card designs for our new company FrostVital based in Los Angeles,California. Both cards will have front and back designs, There is 2 different cards we need designed. I submitted payment of $90. Please let me know if we need to submit another payment..
We liked this designs and I have attached our fav styles named card 1 and card 2.
Brief info about our company, our main service is the Cryotherpahy Chamber, the many benefits of Cryotherapy include overall wellness, weight loss, athletic recovery and beauty & anti-aging. Explanation on benefits is in pic attached. The final design should communicate wellness.
Wording and colors we want on card:
DESIGN card 1-
Colors: white and blues feel free to experiment (the current colors of the card are pretty good with the look we want. We just want to Logo to flow with the color of the card.
FRONT OF CARD:
FrstVital logo ( see attached logos in all formats)
Cryotherapy services
Mark Penterova Owner/Partner
Cell phone icon- 818-555-0193
Office Phone Icon- 805-555-0148
email icon- Mark@frost-vital.example
www.frost-vital.example
————————
2918 W MAPLEFIELD AVE.
CEDAR HOLLOW, CA 90417
BACK OF CARD ( you can play with different colors here as well.) Same concept with the blues whites and grey
Health & Wellness
*
Weight Loss
*
Athletic Recovery
*
Beauty & Anti-Aging
-------------------------------------------------
DESIGN Card 2-
On your current card there is water drops. We are trying to get the concept of a cold theme. Maybe snow flakes instead of water drops. See our attached picture with the machine and Ice/snow theme
FRONT OF CARD:
Cryotherapy services
email icon- Info@frost-vital.example
www.frost-vital.example
————————
WESTLAKE VILLAGE, CA 91362
BACK OF CARD option 1:
20% off your 1st Whole Body Cryo Package
or
50% off First Whole Body Cryo Session
Discover FrostVital!
Just 3 Minutes For Total Body CryoTherapy
* first time Guests only. Certain Restrictions Apply (please put this in very small writing on the bottom of the card )
Back Of Card Option 2 ( I need the same exact thing on the front of the card, same color schemes. The only changes we need is to have on the Back.
1 Free Whole Body Cryo Session
Discover FrostVital!
Certain Restrictions Apply (please put this in very small writing on the bottom of the card )

```html
<!DOCTYPE html>
<html lang="en">
<head>
<meta charset="utf-8">
<title>FrostVital Business Card</title>
<link href="https://fonts.googleapis.com/css2?family=Open+Sans:wght@400;600;700&display=swap" rel="stylesheet">
<style>
  :root {
    --page-bg: #e9ecef;
    --card-dark: #2b2827;
    --card-dark-edge: #3a3634;
    --ice-blue: #35c4f0;
    --ice-blue-deep: #1fb2e2;
    --text-light: #f2f4f5;
    --text-dark: #1b1b1b;
  }
  * { margin: 0; padding: 0; box-sizing: border-box; }
  html, body {
    width: 1200px;
    height: 900px;
    overflow: hidden;
    background: var(--page-bg);
    font-family: "Open Sans", Arial, sans-serif;
  }
  .business-card {
    position: absolute;
    left: 112px;
    top: 150px;
    width: 975px;
    height: 600px;
    border-radius: 22px;
    overflow: hidden;
    background: linear-gradient(160deg, var(--card-dark-edge) 0%, var(--card-dark) 55%, #232120 100%);
    box-shadow: 0 10px 30px rgba(0,0,0,0.18);
  }
  .brand {
    position: absolute;
    left: 78px;
    top: 128px;
    display: flex;
    align-items: center;
    gap: 18px;
  }
  .brand-dot {
    width: 46px;
    height: 46px;
    border-radius: 50%;
    background: var(--ice-blue);
  }
  .brand-name {
    font-size: 56px;
    font-weight: 600;
    color: var(--text-light);
    letter-spacing: -0.5px;
  }
  .contact-person {
    position: absolute;
    left: 552px;
    top: 206px;
  }
  .person-name {
    font-size: 38px;
    font-weight: 600;
    color: var(--ice-blue);
    line-height: 1.05;
  }
  .person-role {
    font-size: 25px;
    color: var(--text-light);
    line-height: 1.1;
  }
  .benefit-list, .contact-list {
    position: absolute;
    top: 318px;
    list-style: none;
  }
  .benefit-list { left: 80px; }
  .contact-list { left: 552px; }
  .benefit-list li, .contact-list li {
    height: 36px;
    display: flex;
    align-items: center;
    font-size: 27px;
    color: var(--text-light);
  }
  .benefit-list li::before {
    content: "";
    width: 13px;
    height: 13px;
    border-radius: 50%;
    background: var(--ice-blue);
    margin-right: 8px;
  }
  .contact-icon {
    width: 26px;
    height: 26px;
    margin-right: 10px;
    flex-shrink: 0;
  }
  .address-band {
    position: absolute;
    left: 0;
    bottom: 0;
    width: 100%;
    height: 114px;
    background: linear-gradient(180deg, var(--ice-blue) 0%, var(--ice-blue-deep) 100%);
    display: flex;
    align-items: center;
    justify-content: center;
  }
  .address-line {
    font-size: 25px;
    color: var(--text-dark);
    letter-spacing: 0.2px;
  }
</style>
</head>
<body>
  <div class="business-card">
    <div class="brand">
      <div class="brand-dot"></div>
      <div class="brand-name">FrostVital</div>
    </div>

    <div class="contact-person">
      <div class="person-name">Mark Penterova</div>
      <div class="person-role">Owner/Partner</div>
    </div>

    <ul class="benefit-list">
      <li>Health &amp; Wellness</li>
      <li>Weight Loss</li>
      <li>Athletic Recovery</li>
      <li>Beauty &amp; Anti-Aging</li>
    </ul>

    <ul class="contact-list">
      <li>
        <svg class="contact-icon" viewBox="0 0 26 26" aria-hidden="true">
          <rect width="26" height="26" rx="5" fill="#35c4f0"/>
          <rect x="8.5" y="4.5" width="9" height="17" rx="1.5" fill="none" stroke="#fff" stroke-width="2"/>
          <circle cx="13" cy="18.3" r="1.1" fill="#fff"/>
        </svg>
        818-555-0193
      </li>
      <li>
        <svg class="contact-icon" viewBox="0 0 26 26" aria-hidden="true">
          <rect width="26" height="26" rx="5" fill="#35c4f0"/>
          <path d="M5 10.5c0-2.5 3.5-4 8-4s8 1.5 8 4v1.5h-4v-2h-8v2H5z" fill="#fff"/>
          <rect x="7" y="13" width="12" height="7" rx="1.5" fill="#fff"/>
        </svg>
        805-555-0148
      </li>
      <li>
        <svg class="contact-icon" viewBox="0 0 26 26" aria-hidden="true">
          <rect width="26" height="26" rx="5" fill="#35c4f0"/>
          <rect x="5" y="8" width="16" height="11" rx="1" fill="#fff"/>
          <path d="M5.5 8.5l7.5 6 7.5-6" fill="none" stroke="#35c4f0" stroke-width="1.6"/>
        </svg>
        Mark@frost-vital.example
      </li>
      <li>
        <svg class="contact-icon" viewBox="0 0 26 26" aria-hidden="true">
          <rect width="26" height="26" rx="5" fill="#35c4f0"/>
          <g fill="none" stroke="#fff" stroke-width="2.2" stroke-linecap="round">
            <path d="M11.5 14.5l3-3"/>
            <path d="M12 9.5l1.8-1.8a3 3 0 0 1 4.5 4.5l-1.8 1.8"/>
            <path d="M14 16.5l-1.8 1.8a3 3 0 0 1-4.5-4.5l1.8-1.8"/>
          </g>
        </svg>
        www.frost-vital.example
      </li>
    </ul>

    <div class="address-band">
      <p class="address-line">2918 W MAPLEFIELD AVE. CEDAR HOLLOW, CA 90417</p>
    </div>
  </div>
</body>
</html>
```